Meridian Handsets business card design

I would like to see some designs for a business card for Meridian Handsets. I would like the business card to be double sided. It will need to have a similar colour / look and feel to our website www.meridianhandsets.com.au I have also attached our latest flyer. Final designs to be handed over in Photoshop format so that I can edit the business card when needed please.

Industry/Entity Type

Business

Contact Information for Business Card

Gavin Thornley
sales@meridianhandsets.com.au
Business Development Manager
ph: (08) 6197 5821
www.meridianhandsets.com.au

Font styles to use
Serif
Sans Serif

Requirements
Must have
• If you could please utilise our colour scheme as seen on our website and the attached flyer.
• I would also like the final design to be in a Photoshop format so that I can edit it when needed please.

```html
<!DOCTYPE html>
<html lang="en">
<head>
<meta charset="utf-8">
<title>Meridian Handsets – Business Card</title>
<link rel="stylesheet" href="https://fonts.googleapis.com/css2?family=Open+Sans:wght@400;600;700&display=swap">
<style>
  :root {
    --stage: #e9e9eb;
    --card-white: #ffffff;
    --card-black: #0b0b0b;
    --ink: #2e2e30;
    --ink-soft: #444446;
    --brand-blue: #0f7fbf;
    --band-dark: #2d2d2f;
    --on-dark: #ffffff;
  }
  * { box-sizing: border-box; margin: 0; padding: 0; }
  html, body {
    width: 1200px;
    height: 900px;
    overflow: hidden;
    background: var(--stage);
    font-family: "Open Sans", Arial, sans-serif;
  }
  .canvas {
    position: relative;
    width: 1200px;
    height: 900px;
  }
  .card {
    position: absolute;
    left: 280px;
    width: 640px;
    height: 366px;
    overflow: hidden;
    box-shadow: 0 6px 18px rgba(0,0,0,0.15);
  }
  .card--back {
    top: 50px;
    background: var(--card-black);
    display: flex;
    align-items: center;
    justify-content: center;
  }
  .card--front {
    top: 476px;
    background: var(--card-white);
  }
  .wordmark {
    font-weight: 600;
    font-size: 50px;
    letter-spacing: -0.5px;
    line-height: 1;
    white-space: nowrap;
  }
  .card--back .wordmark { color: var(--on-dark); }
  .card--front .wordmark {
    position: absolute;
    left: 262px;
    top: 146px;
    font-size: 40px;
    color: var(--ink);
  }
  .corner-mark {
    position: absolute;
    left: 0;
    top: 0;
    width: 56px;
    height: 40px;
  }
  .identity {
    position: absolute;
    left: 64px;
    top: 10px;
  }
  .identity__name {
    color: var(--brand-blue);
    font-weight: 700;
    font-size: 17px;
    line-height: 1.15;
  }
  .identity__role {
    color: var(--ink-soft);
    font-size: 13px;
    line-height: 1.2;
  }
  .contacts {
    position: absolute;
    left: 26px;
    top: 206px;
    list-style: none;
  }
  .contacts__item {
    display: flex;
    align-items: center;
    gap: 10px;
    color: var(--ink);
    font-size: 15px;
    line-height: 22px;
  }
  .contacts__icon {
    width: 12px;
    height: 12px;
    flex: none;
  }
  .base-bands {
    position: absolute;
    left: 0;
    bottom: 0;
    width: 640px;
    height: 34px;
  }
</style>
</head>
<body>
  <main class="canvas">
    <section class="card card--back" aria-label="Card back">
      <p class="wordmark">MeridianHandsets</p>
    </section>

    <section class="card card--front" aria-label="Card front">
      <svg class="corner-mark" viewBox="0 0 56 40" aria-hidden="true">
        <polygon points="0,0 26,0 0,26" fill="var(--brand-blue)"/>
        <polygon points="30,0 56,0 42,40 16,40" fill="var(--band-dark)"/>
      </svg>

      <div class="identity">
        <p class="identity__name">Gavin Thornley</p>
        <p class="identity__role">Business Development Manager</p>
      </div>

      <p class="wordmark">MeridianHandsets</p>

      <ul class="contacts">
        <li class="contacts__item">
          <svg class="contacts__icon" viewBox="0 0 12 12" aria-hidden="true">
            <path d="M2.5 0.8 L4.4 2.9 L3.4 4.3 C4.1 5.8 5.2 7 6.8 7.8 L8.1 6.8 L10.3 8.6 L9.2 10.8 C4.9 10.4 1.3 6.8 0.9 2.2 Z" fill="var(--brand-blue)"/>
          </svg>
          (08) 6197 5821
        </li>
        <li class="contacts__item">
          <svg class="contacts__icon" viewBox="0 0 12 12" aria-hidden="true">
            <rect x="0.5" y="2" width="11" height="8" fill="var(--brand-blue)"/>
            <path d="M0.8 2.4 L6 6.6 L11.2 2.4" fill="none" stroke="#fff" stroke-width="1"/>
          </svg>
          sales@meridianhandsets.com.au
        </li>
        <li class="contacts__item">
          <svg class="contacts__icon" viewBox="0 0 12 12" aria-hidden="true">
            <circle cx="6" cy="6" r="5.5" fill="var(--brand-blue)"/>
            <path d="M0.5 6 H11.5 M6 0.5 C3 3 3 9 6 11.5 M6 0.5 C9 3 9 9 6 11.5" fill="none" stroke="#fff" stroke-width="0.8"/>
          </svg>
          www.meridianhandsets.com.au
        </li>
      </ul>

      <svg class="base-bands" viewBox="0 0 640 34" preserveAspectRatio="none" aria-hidden="true">
        <polygon points="0,10 300,10 290,34 0,34" fill="var(--band-dark)"/>
        <polygon points="310,0 640,0 640,34 296,34" fill="var(--brand-blue)"/>
      </svg>
    </section>
  </main>
</body>
</html>
```